2 banners on the outside wall of the hall

Banner 1:
Kalvamo specializes in the planning, construction, and maintenance of high-quality pond systems, particularly swimming ponds, natural pools, garden ponds, koi ponds, streams, and waterfalls. Learn more at www.kalvamo.de
The following data should be included:
Planning and construction of swimming ponds and natural pools, as well as garden ponds and koi ponds
100% organic
Individually planned
Over 20 years of experience
04271 6632907
www.kalvamo.de
“Logo-Kalvamo”
Banner 2:
Lumo-Grün is the online shop for high-quality aquatic plants for ponds and aquariums.
More information at https://lumo-gruen.de
Online shop for pond plants and water lilies, as well as aquarium plants and accessories
Over 400 plant species
Top gardener quality
Secure packaging & fast shipping
04271 6632906
www.lumo-gruen. de
“Logo Lumo green”
Here's roughly what we envision:
The designs for each banner should be clearly visible and include everything needed, without appearing cluttered. In other words, it should be immediately clear what the banner is about.
We should also be made aware of our unique selling points and advantages.
It is important that the banners also harmonize visually with each other.
We liked the banner image in the attachment and it serves as inspiration.
The banner print data is produced as follows:
• Banner size: Width x Height: 3880 mm x 1880 mm
• Material: Mesh banner, PVFormat: PDF (X-3:2000)
• Fonts: converted into paths
• Trim allowance: +2 mm all around
• Color space: CMYK
• Resolution: 72 dpi (recommended) at 1:1 resolution
Look and feel
Each slider illustrates characteristics of the customer's brand and the style your logo design should communicate.

```html
<!DOCTYPE html>
<html lang="de">
<head>
<meta charset="utf-8">
<title>Kalvamo Banner</title>
<link rel="stylesheet" href="https://fonts.googleapis.com/css2?family=Barlow:wght@600;700&family=Montserrat:wght@500;700&family=Open+Sans:wght@400&display=swap">
<style>
  :root {
    --navy: #1d3d5e;
    --brand-blue: #2a5d8c;
    --band-blue: rgba(52, 98, 150, 0.9);
    --leaf-green: #7fc241;
    --frame: #1a1a1a;
    --paper: #ffffff;
    --photo-top: #9a5a3e;
    --photo-mid: #567e4a;
    --photo-water: #5d7a86;
    --photo-shore: #b3a590;
  }
  * { margin: 0; padding: 0; box-sizing: border-box; }
  html, body { width: 1200px; height: 667px; overflow: hidden; background: var(--paper); }
  .canvas { position: relative; width: 1200px; height: 667px; background: var(--paper); }

  .size-label {
    position: absolute; left: 937px; top: 12px;
    font: 400 21px "Open Sans", sans-serif; color: var(--brand-blue);
  }

  .pond-photo {
    position: absolute; left: 403px; top: 75px; width: 728px; height: 522px;
    background: linear-gradient(180deg, var(--photo-top) 0%, var(--photo-mid) 35%, var(--photo-water) 65%, var(--photo-shore) 100%);
  }

  .banner-frame {
    position: absolute; left: 83px; top: 83px; width: 1043px; height: 505px;
    border: 1px solid var(--frame);
  }

  .brand-name {
    position: absolute; left: 83px; width: 320px; top: 112px;
    text-align: center;
    font: 700 52px "Montserrat", sans-serif; color: var(--brand-blue);
    letter-spacing: -0.5px;
  }

  .green-rule {
    position: absolute; left: 119px; width: 244px; height: 3px;
    background: var(--leaf-green); border-radius: 2px;
  }
  .green-rule.top { top: 224px; }
  .green-rule.bottom { top: 440px; }

  .usp-list { position: absolute; left: 107px; top: 249px; list-style: none; }
  .usp-item {
    position: relative; padding-left: 38px; margin-bottom: 15px;
    font: 700 35px/29px "Barlow", sans-serif; color: var(--navy);
  }
  .usp-item .tick { position: absolute; left: 0; top: 0; width: 29px; height: 29px; }

  .contact { position: absolute; left: 83px; width: 320px; top: 488px; text-align: center; }
  .contact .phone { font: 700 40px/40px "Barlow", sans-serif; color: var(--navy); letter-spacing: 0.5px; }
  .contact .web { font: 500 29px/30px "Montserrat", sans-serif; color: var(--navy); }

  .service-band { position: absolute; left: 470px; top: 276px; width: 590px; }
  .service-line {
    display: block; height: 37px; margin-bottom: 4px;
    background: var(--band-blue);
    text-align: center;
    font: 700 27px/37px "Montserrat", sans-serif; color: #ffffff;
    white-space: nowrap;
  }
</style>
</head>
<body>
<div class="canvas">
  <div class="size-label">3880mm x 1880mm</div>

  <div class="pond-photo" role="img" aria-label="Foto: naturnaher Schwimmteich mit Kiesufer und Gräsern, dahinter Backsteinhaus mit Holzterrasse"></div>

  <div class="banner-frame"></div>

  <div class="brand-name">Kalvamo</div>

  <div class="green-rule top"></div>

  <ul class="usp-list">
    <li class="usp-item">
      <svg class="tick" viewBox="0 0 30 30"><rect x="2" y="7" width="20" height="20" fill="none" stroke="#1d3d5e" stroke-width="3.5"/><path d="M7 15 L12 21 L27 2" fill="none" stroke="#1d3d5e" stroke-width="3.5" stroke-linecap="round" stroke-linejoin="round"/></svg>
      100% biologisch
    </li>
    <li class="usp-item">
      <svg class="tick" viewBox="0 0 30 30"><rect x="2" y="7" width="20" height="20" fill="none" stroke="#1d3d5e" stroke-width="3.5"/><path d="M7 15 L12 21 L27 2" fill="none" stroke="#1d3d5e" stroke-width="3.5" stroke-linecap="round" stroke-linejoin="round"/></svg>
      Individuell<br>geplant
    </li>
    <li class="usp-item">
      <svg class="tick" viewBox="0 0 30 30"><rect x="2" y="7" width="20" height="20" fill="none" stroke="#1d3d5e" stroke-width="3.5"/><path d="M7 15 L12 21 L27 2" fill="none" stroke="#1d3d5e" stroke-width="3.5" stroke-linecap="round" stroke-linejoin="round"/></svg>
      Über 20 Jahre<br>Erfahrung
    </li>
  </ul>

  <div class="green-rule bottom"></div>

  <div class="contact">
    <div class="phone">04271 6632907</div>
    <div class="web">www.kalvamo.de</div>
  </div>

  <div class="service-band">
    <span class="service-line">Planung und Bau von Schwimmteichen</span>
    <span class="service-line">und Naturpools sowie Gartenteichen</span>
    <span class="service-line">und Koiteichen</span>
  </div>
</div>
</body>
</html>
```